Fire Hydrant Repair Parts Flyer

We need a flyer advertising both fire hydrant parts and the manufacturers that we are stocking. Our company is Coastal Flowline Supply and we are a parts distributor who sells directly to contractors. I have attached an example flyer that advertises some other parts we stock. We don't want it to look exactly like the old flyer, but we would like it to be structured similarly. I have also attached a background image for the flyer as well as some pictures of the parts we are stocking. I have also attached pictures of the manufacturer logos that we are stocking. We are trying to convey the parts that we are stocking which are: "Traffic Repair Kits", "Main Valve Repair Kits", "Extension Kits", "Replacement Caps & Gaskets", "Replacement Nozzles", Adjustable Hydrant Wrenches", "Hydrant Diffusers", & "Hydrant Oil". I have attached pictures of some of these items that we would like placed on the flyer. Let me know if you have any questions at all.

```html
<!DOCTYPE html>
<html lang="en">
<head>
<meta charset="utf-8">
<title>Fire Hydrant Repair Parts Flyer</title>
<link rel="stylesheet" href="https://fonts.googleapis.com/css2?family=Oswald:wght@700&family=Poppins:wght@400;500;600;700&display=swap">
<style>
  :root{
    --navy:#16226b;
    --blue:#3a4ea3;
    --red:#e8184f;
    --grey:#e5e5e7;
    --card-grey:#e3e4e8;
    --ink:#1b1f3a;
    --page:#f2f2f3;
    --white:#ffffff;
  }
  *{box-sizing:border-box;margin:0;padding:0}
  html,body{width:1200px;height:2488px;overflow:hidden;background:var(--page)}
  body{font-family:"Poppins",sans-serif;position:relative}
  .flyer{
    position:absolute;left:40px;top:519px;width:861px;height:1114px;
    background:var(--white);transform:scale(1.3);transform-origin:0 0;
    box-shadow:0 8px 24px rgba(0,0,0,.18);overflow:hidden;
  }
  .abs{position:absolute}
  .header-bg{left:0;top:0;width:861px;height:368px}
  .brand{left:50px;top:52px;display:flex;align-items:center;gap:12px}
  .brand-dot{width:22px;height:22px;border-radius:50%;background:var(--red)}
  .brand-name{font-size:25px;font-weight:500;color:var(--blue);line-height:1}
  .title{left:50px;top:118px;font-family:"Oswald",sans-serif;font-weight:700;font-size:74px;line-height:1;letter-spacing:-1px}
  .title .fire{color:var(--red)}
  .title .hydrant{color:var(--navy)}
  .repair{left:50px;top:204px;width:328px;height:52px;background:var(--red);color:var(--white);
    font-weight:700;font-size:40px;line-height:52px;padding-left:14px;letter-spacing:.5px}
  .intro{left:50px;top:268px;width:340px;font-size:13.2px;font-weight:600;color:var(--navy);line-height:16px}
  .section-bar{left:51px;width:757px;height:47px}
  .section-bar span{position:absolute;left:21px;top:0;line-height:47px;color:var(--white);font-weight:600;font-size:26px}
  .checklist{left:50px;top:490px;list-style:none}
  .checklist li{display:flex;align-items:center;height:41px}
  .checklist svg{width:17px;height:17px;margin-right:12px}
  .checklist .item{width:303px;height:32px;border:1.5px solid #c9c9cf;padding-left:15px;line-height:29px;
    font-size:17px;font-weight:600;color:var(--ink)}
  .product{width:123px}
  .product .photo{width:123px;height:118px;border-radius:4px}
  .product .label{height:42px;margin-top:10px;display:flex;align-items:center;justify-content:center;text-align:center;
    font-size:11.5px;font-weight:600;line-height:14px}
  .label.red{background:var(--red);color:var(--white)}
  .label.grey{background:var(--card-grey);color:var(--navy)}
  .makers{left:60px;top:935px;width:740px;height:50px;display:flex;align-items:center;justify-content:space-between}
  .maker{font-weight:700;font-size:18px;color:var(--navy)}
  .footer{left:0;top:1015px;width:861px;height:99px}
  .help{left:50px;top:1030px;color:var(--white)}
  .help h3{font-size:19px;font-weight:600;line-height:24px}
  .contact{left:50px;top:1058px;display:flex;align-items:center;color:var(--white);font-size:11.5px;height:34px}
  .contact .sep{width:1px;height:34px;background:rgba(255,255,255,.6);margin:0 18px}
  .contact strong{font-weight:600;margin-left:6px}
  .contact svg{width:14px;height:14px;margin-right:8px}
</style>
</head>
<body>
<div class="flyer">
  <!-- header shapes -->
  <svg class="abs header-bg" viewBox="0 0 861 368" aria-hidden="true">
    <rect width="861" height="368" fill="#e5e5e7"/>
    <polygon points="436,0 861,0 861,368 470,368" fill="#e8184f"/>
    <polygon points="0,355 466,355 468,368 0,368" fill="#16226b"/>
  </svg>
  <div class="abs" role="img" aria-label="Photo of a red fire hydrant flushing water onto grass"
       style="left:0;top:0;width:861px;height:355px;clip-path:polygon(447px 0,861px 0,861px 355px,491px 355px);
       background:linear-gradient(90deg,#dfe3e6 0%,#c8cfc8 45%,#b51b22 70%,#6d8f3c 100%)"></div>

  <div class="abs brand"><span class="brand-dot"></span><span class="brand-name">Coastal Flowline Supply</span></div>
  <h1 class="abs title"><span class="fire">FIRE</span> <span class="hydrant">HYDRANT</span></h1>
  <div class="abs repair">REPAIR PARTS</div>
  <p class="abs intro">Our company is Coastal Flowline Supply and we are a parts distributor who sells directly to contractors.</p>

  <!-- products -->
  <svg class="abs section-bar" style="top:399px" viewBox="0 0 757 47" aria-hidden="true"><polygon points="0,0 753,0 757,47 0,47" fill="#3a4ea3"/></svg>
  <div class="abs section-bar" style="top:399px"><span>Products we are Stocking</span></div>

  <ul class="abs checklist">
    <li><svg viewBox="0 0 17 17"><circle cx="8" cy="9" r="6.5" fill="none" stroke="#3a4ea3" stroke-width="1.5"/><path d="M5 9l3 3 7-8" fill="none" stroke="#e8184f" stroke-width="2"/></svg><span class="item">Traffic Repair Kits</span></li>
    <li><svg viewBox="0 0 17 17"><circle cx="8" cy="9" r="6.5" fill="none" stroke="#3a4ea3" stroke-width="1.5"/><path d="M5 9l3 3 7-8" fill="none" stroke="#e8184f" stroke-width="2"/></svg><span class="item">Main Valve Repair Kits</span></li>
    <li><svg viewBox="0 0 17 17"><circle cx="8" cy="9" r="6.5" fill="none" stroke="#3a4ea3" stroke-width="1.5"/><path d="M5 9l3 3 7-8" fill="none" stroke="#e8184f" stroke-width="2"/></svg><span class="item">Extension Kits</span></li>
    <li><svg viewBox="0 0 17 17"><circle cx="8" cy="9" r="6.5" fill="none" stroke="#3a4ea3" stroke-width="1.5"/><path d="M5 9l3 3 7-8" fill="none" stroke="#e8184f" stroke-width="2"/></svg><span class="item">Replacement Caps &amp; Gaskets</span></li>
    <li><svg viewBox="0 0 17 17"><circle cx="8" cy="9" r="6.5" fill="none" stroke="#3a4ea3" stroke-width="1.5"/><path d="M5 9l3 3 7-8" fill="none" stroke="#e8184f" stroke-width="2"/></svg><span class="item">Replacement Nozzles</span></li>
    <li><svg viewBox="0 0 17 17"><circle cx="8" cy="9" r="6.5" fill="none" stroke="#3a4ea3" stroke-width="1.5"/><path d="M5 9l3 3 7-8" fill="none" stroke="#e8184f" stroke-width="2"/></svg><span class="item">Adjustable Hydrant Wrenches</span></li>
    <li><svg viewBox="0 0 17 17"><circle cx="8" cy="9" r="6.5" fill="none" stroke="#3a4ea3" stroke-width="1.5"/><path d="M5 9l3 3 7-8" fill="none" stroke="#e8184f" stroke-width="2"/></svg><span class="item">Hydrant Diffusers</span></li>
    <li><svg viewBox="0 0 17 17"><circle cx="8" cy="9" r="6.5" fill="none" stroke="#3a4ea3" stroke-width="1.5"/><path d="M5 9l3 3 7-8" fill="none" stroke="#e8184f" stroke-width="2"/></svg><span class="item">Hydrant Oil</span></li>
  </ul>

  <div class="abs product" style="left:417px;top:462px">
    <div class="photo" role="img" aria-label="Yellow hydrant diffuser with pressure gauge" style="background:radial-gradient(circle,#f2b21c 0%,#fbe8b8 55%,#fff 75%)"></div>
    <div class="label red">Hydrant Diffuser</div>
  </div>
  <div class="abs product" style="left:552px;top:462px">
    <div class="photo" role="img" aria-label="Black fire hydrant extension kit with bolts" style="background:radial-gradient(circle,#3b3d40 0%,#b9bbbe 55%,#fff 75%)"></div>
    <div class="label grey">Fire Hydrant<br>Extension Kit Pic</div>
  </div>
  <div class="abs product" style="left:687px;top:462px">
    <div class="photo" role="img" aria-label="Red fire hydrant cap with steel chain" style="background:radial-gradient(circle,#d8262f 0%,#e8c3c5 50%,#fff 75%)"></div>
    <div class="label red">Fire Hydrant<br>Cap and Chain</div>
  </div>
  <div class="abs product" style="left:417px;top:660px">
    <div class="photo" role="img" aria-label="White bottle of hydrant lubricant oil" style="background:radial-gradient(circle,#e9e9ea 0%,#f6f6f6 55%,#fff 75%)"></div>
    <div class="label grey">Lube Picture</div>
  </div>
  <div class="abs product" style="left:552px;top:660px">
    <div class="photo" role="img" aria-label="Silver adjustable fire hydrant wrench" style="background:radial-gradient(circle,#a7aaae 0%,#e3e4e6 50%,#fff 75%)"></div>
    <div class="label red">Fire Hydrant<br>Wrench</div>
  </div>
  <div class="abs product" style="left:687px;top:660px">
    <div class="photo" role="img" aria-label="Hydrant traffic repair kit with coupling and bolts" style="background:radial-gradient(circle,#2e3033 0%,#aeb0b3 55%,#fff 75%)"></div>
    <div class="label grey">Hydrant Traffic<br>Repair Kit Pic</div>
  </div>

  <!-- manufacturers -->
  <svg class="abs section-bar" style="top:860px" viewBox="0 0 757 47" aria-hidden="true"><polygon points="0,0 753,0 757,47 0,47" fill="#16226b"/></svg>
  <div class="abs section-bar" style="top:860px"><span style="left:24px">Manufacturer&nbsp; we are Stocking</span></div>

  <div class="abs makers">
    <span class="maker">Harbor Pipe</span>
    <span class="maker">Union Flow</span>
    <span class="maker">Ridgeway</span>
    <span class="maker">Stanton Valve</span>
    <span class="maker">Kestrel</span>
    <span class="maker">Brennan</span>
  </div>

  <!-- footer -->
  <svg class="abs footer" viewBox="0 0 861 99" aria-hidden="true">
    <polygon points="0,0 822,0 822,99 0,99" fill="#3a4ea3"/>
    <polygon points="822,0 851,99 822,99" fill="#e8184f"/>
  </svg>
  <div class="abs help"><h3>Need Help?</h3></div>
  <div class="abs contact">
    <span>Please Call Us At:</span>
    <svg viewBox="0 0 14 14" style="margin:0 0 0 8px"><path d="M3 1l2.5 2.5-1.2 1.8c.8 1.8 2.2 3.2 4 4l1.8-1.2L12.6 10.6 11 12.8C6 12.5 1.5 8 1.2 3z" fill="#e8184f"/></svg>
    <strong>(800) 555-0142</strong>
    <span class="sep"></span>
    <svg viewBox="0 0 14 14"><rect x="1" y="3" width="12" height="9" fill="#e8184f"/><path d="M1 3l6 5 6-5" fill="none" stroke="#fff" stroke-width="1"/></svg>
    <span>service@coastalflowline.com</span>
    <span class="sep"></span>
    <svg viewBox="0 0 14 14"><circle cx="7" cy="7" r="6" fill="none" stroke="#e8184f" stroke-width="1.5"/><path d="M1 7h12M7 1c-3 3-3 9 0 12M7 1c3 3 3 9 0 12" fill="none" stroke="#e8184f" stroke-width="1"/></svg>
    <span>www.<strong style="margin:0">coastalflowline</strong>.com</span>
  </div>
</div>
</body>
</html>
```